Fernvale Business Card Design

We are looking for a fresh business card design for our new logo. We would like a business card that is unique but friendly. We are in the window coverings business offering blinds, shutters and shades for homes.

Target Market(s)

Targeting the end-consumer

Industry/Entity Type

Business

Requirements
Must have
• Must have a dedicates space for a photo of our sales person. Must contain our new logo (attached).

```html
<!DOCTYPE html>
<html lang="en">
<head>
<meta charset="utf-8">
<title>Fernvale Business Card</title>
<link rel="stylesheet" href="https://fonts.googleapis.com/css2?family=Roboto:wght@400;500&family=Roboto+Condensed:wght@700&display=swap">
<style>
  :root {
    --backdrop: #3a3a3b;
    --card: #2a2a2b;
    --card-edge: #323233;
    --accent: #92c83e;
    --text-light: #f2f2f2;
    --text-muted: #9a9a9a;
    --logo-grey: #c9c9c9;
    --portrait-tone: #4c4c4e;
    --portrait-shade: #444446;
  }
  * { margin: 0; padding: 0; box-sizing: border-box; }
  html, body { width: 1200px; height: 900px; overflow: hidden; }
  body {
    background: var(--backdrop);
    font-family: "Roboto", Arial, sans-serif;
    position: relative;
  }
  .card {
    position: absolute;
    left: 260px;
    width: 680px;
    height: 380px;
    background: var(--card);
    border: 1px solid var(--card-edge);
    overflow: hidden;
  }
  .card-front { top: 50px; }
  .card-back { top: 470px; }

  .brand { position: absolute; left: 110px; top: 62px; }
  .brand-row { display: flex; align-items: center; gap: 12px; }
  .brand-square {
    width: 38px; height: 38px;
    border: 3px solid var(--logo-grey);
    border-radius: 4px;
  }
  .brand-name {
    font-size: 38px; font-weight: 400;
    color: var(--logo-grey); letter-spacing: 0.5px;
  }
  .brand-url {
    margin-top: 8px;
    font-size: 13px; letter-spacing: 6.5px;
    color: var(--text-light);
  }
  .portrait {
    position: absolute;
    right: 20px; bottom: 0;
    width: 270px; height: 270px;
    background: linear-gradient(180deg, var(--portrait-tone), var(--portrait-shade));
    border-radius: 90px 90px 0 0;
  }

  .identity {
    position: absolute; right: 370px; top: 145px;
    text-align: right;
  }
  .person-name {
    font-family: "Roboto Condensed", "Arial Narrow", sans-serif;
    font-weight: 700; font-size: 34px;
    color: var(--accent); line-height: 1;
  }
  .person-role {
    font-size: 17px; color: var(--text-muted);
    margin-top: 4px; letter-spacing: 0.3px;
  }
  .divider {
    position: absolute; left: 330px; top: 140px;
    width: 2px; height: 110px;
    background: var(--text-muted);
  }
  .contacts {
    position: absolute; left: 352px; top: 140px;
    list-style: none;
  }
  .contacts li {
    display: flex; align-items: center; gap: 9px;
    font-size: 16px; font-weight: 500;
    color: var(--text-light); height: 22px;
  }
  .contacts svg, .address svg { width: 14px; height: 14px; flex: none; fill: var(--accent); }
  .address {
    position: absolute; left: 110px; top: 300px;
    display: flex; align-items: center; gap: 6px;
    font-size: 17px; font-weight: 500; color: var(--text-light);
  }
</style>
</head>
<body>
  <section class="card card-front">
    <div class="brand">
      <div class="brand-row">
        <span class="brand-square"></span>
        <span class="brand-name">Fernvale</span>
      </div>
      <div class="brand-url">www.fernvale.com</div>
    </div>
    <div class="portrait" role="img" aria-label="Space for a portrait photo of the sales person in suit and tie"></div>
  </section>

  <section class="card card-back">
    <div class="identity">
      <div class="person-name">MARK ELLISON</div>
      <div class="person-role">CEO/FOUNDER</div>
    </div>
    <div class="divider"></div>
    <ul class="contacts">
      <li><svg viewBox="0 0 16 16"><path d="M3 1h3l1.5 4-2 1.3a9 9 0 0 0 4.2 4.2L11 8.5l4 1.5v3a2 2 0 0 1-2 2A12 12 0 0 1 1 3a2 2 0 0 1 2-2z"/></svg>612 555 0147</li>
      <li><svg viewBox="0 0 16 16"><path d="M4 0h8a1 1 0 0 1 1 1v14a1 1 0 0 1-1 1H4a1 1 0 0 1-1-1V1a1 1 0 0 1 1-1zm1 2v10h6V2zm3 11a1 1 0 1 0 0 2 1 1 0 0 0 0-2z"/></svg>612 555 0183</li>
      <li><svg viewBox="0 0 16 16"><path d="M4 0h7v4H4zM1 5h14a1 1 0 0 1 1 1v6a1 1 0 0 1-1 1h-2v3H3v-3H1a1 1 0 0 1-1-1V6a1 1 0 0 1 1-1zm4 6v3h6v-3z"/></svg>612 555 0129</li>
      <li><svg viewBox="0 0 16 16"><path d="M0 3h16v1.2L8 9 0 4.2zM0 6l8 4.8L16 6v7H0z"/></svg>name@fernvale.com</li>
      <li><svg viewBox="0 0 16 16"><circle cx="8" cy="8" r="8"/><path d="M1 8h14M8 1c-3 3-3 11 0 14M8 1c3 3 3 11 0 14" stroke="#2a2a2b" stroke-width="1.2" fill="none"/></svg>www.fernvale.com</li>
    </ul>
    <div class="address">
      <svg viewBox="0 0 16 16"><path d="M8 0a6 6 0 0 1 6 6c0 4.5-6 10-6 10S2 10.5 2 6a6 6 0 0 1 6-6zm0 3.5a2.5 2.5 0 1 0 0 5 2.5 2.5 0 0 0 0-5z"/></svg>
      2143 Willow Bend Road, Juneau, Alaska 34512
    </div>
  </section>
</body>
</html>
```